Food Safety Consultancy Flyer Design

We need a flyer design for a new company called Tundo Training. New food safety regulations are coming into effect for all food operators in March 2016. My company provides training and resources to support food operators during the transition onto the new Food Control Plan. For the designs we would like to see any of the colours used from the logo which is attached. The flyer will be letting operators know that there are new regulations and we are here to help. Our company offers three packages: 1. Videos (training videos) 2. Webinars and Workshop 3. One-on-one mentoring. Our websites main colour used is the green colour from the logo.
Food service operators: cafes, restaurants etc.
Hospitality

```html
<!DOCTYPE html>
<html lang="en">
<head>
<meta charset="utf-8">
<title>Tundo Training – Food Act 2014 Flyer</title>
<link rel="stylesheet" href="https://fonts.googleapis.com/css2?family=Teko:wght@500;600&family=Open+Sans:ital,wght@0,400;0,600;1,400&display=swap">
<style>
  :root{
    --green:#2DA146;
    --blue:#1D72BF;
    --charcoal:#2E2E30;
    --ink:#2b2b2b;
    --orange:#F0951E;
    --paper:#ffffff;
    --mist:#ecedef;
    --backdrop:#d9d9d9;
  }
  *{box-sizing:border-box;margin:0;padding:0}
  html,body{width:825px;height:1200px;overflow:hidden;background:var(--backdrop)}
  .flyer{
    position:absolute;left:76px;top:125px;width:673px;height:950px;
    background:linear-gradient(180deg,var(--paper) 0%,var(--paper) 50%,var(--mist) 62%,var(--paper) 80%,var(--paper) 100%);
    overflow:hidden;font-family:"Open Sans",Arial,sans-serif;
  }
  .hero-photo{
    position:absolute;left:0;top:0;width:400px;height:420px;
    background:linear-gradient(135deg,#f3f1ee 0%,#e6ddd4 35%,#c99f86 55%,#e8e4df 75%,#f4f4f4 100%);
  }
  .hero-shapes{position:absolute;left:0;top:0;width:673px;height:460px}
  .announce{
    position:absolute;right:28px;top:42px;width:300px;text-align:right;white-space:nowrap;
    font-family:"Teko","Arial Narrow",sans-serif;font-weight:500;
    font-size:52px;line-height:58px;
  }
  .announce .light{color:var(--paper)}
  .announce .dark{color:var(--ink)}
  .announce-note{
    position:absolute;right:28px;top:288px;width:226px;
    text-align:justify;text-align-last:right;
    color:var(--paper);font-style:italic;font-size:13.5px;line-height:19.5px;
  }
  .tagline{
    position:absolute;left:36px;top:455px;white-space:nowrap;
    font-family:"Teko","Arial Narrow",sans-serif;font-weight:500;color:var(--ink);
    font-size:32px;line-height:36px;
  }
  .tagline-strong{
    display:block;color:var(--blue);font-size:64px;line-height:60px;font-weight:600;
  }
  .brand{
    position:absolute;left:480px;top:500px;
    display:flex;align-items:center;gap:8px;white-space:nowrap;
  }
  .brand-dot{width:24px;height:24px;border-radius:50%;background:var(--orange);flex:none}
  .brand-name{
    font-family:"Open Sans",Arial,sans-serif;font-weight:600;color:var(--ink);
    font-size:15px;letter-spacing:1px;text-transform:uppercase;line-height:20px;
  }
  .packages{position:absolute;left:26px;top:582px;width:619px;height:151px;display:flex;box-shadow:0 6px 8px rgba(0,0,0,.12)}
  .package{padding:12px 14px;color:#e9f0f8}
  .package--videos{width:201px;background:var(--blue)}
  .package--webinars{width:235px;background:var(--charcoal)}
  .package--mentoring{width:183px;background:var(--blue)}
  .package-title{
    font-family:"Teko","Arial Narrow",sans-serif;font-weight:500;color:var(--paper);
    font-size:23px;line-height:26px;text-align:center;white-space:nowrap;
  }
  .package-title span{display:inline-block;border-bottom:1.5px solid var(--paper);padding:0 4px 3px}
  .package-text{margin-top:12px;font-style:italic;font-size:11.5px;line-height:16px}
  .knowledge-title{
    position:absolute;left:36px;top:762px;
    font-family:"Teko","Arial Narrow",sans-serif;font-weight:500;color:var(--blue);font-size:26px;
  }
  .knowledge{
    position:absolute;left:40px;top:800px;display:flex;gap:14px;
  }
  .knowledge-list{
    list-style:none;font-style:italic;font-size:14.5px;line-height:20.5px;color:var(--ink);
  }
  .knowledge-list--first{width:168px}
  .knowledge-list--second{width:200px}
  .knowledge-list li{position:relative;padding-left:15px}
  .knowledge-list li::before{
    content:"";position:absolute;left:0;top:7px;width:7px;height:7px;border-radius:50%;background:var(--green);
  }
  .call{
    position:absolute;left:451px;top:765px;width:195px;height:112px;
    background:var(--orange);border-radius:14px 0 14px 14px;text-align:center;color:var(--ink);
  }
  .call-tab{position:absolute;right:0;top:-18px;width:40px;height:20px}
  .call-label{font-family:"Teko","Arial Narrow",sans-serif;font-weight:600;font-size:56px;line-height:56px;margin-top:16px}
  .call-number{font-family:"Open Sans",Arial,sans-serif;font-weight:600;color:var(--paper);font-size:27px;line-height:30px}
  .footer-rule{position:absolute;left:0;top:884px;width:673px;height:3px;background:var(--charcoal)}
  .footer{
    position:absolute;left:0;top:891px;width:673px;height:59px;background:var(--green);
    color:var(--paper);font-style:italic;font-size:16px;padding:15px 36px;white-space:nowrap;
  }
</style>
</head>
<body>
<main class="flyer">
  <div class="hero-photo" role="img" aria-label="Photo of a chef garnishing a plated strawberry dessert with mint"></div>

  <svg class="hero-shapes" viewBox="0 0 673 460" aria-hidden="true">
    <polygon points="0,392 196,420 420,392 420,408 196,436 0,408" fill="var(--orange)"/>
    <polygon points="0,408 196,436 420,408 420,420 0,420" fill="#ffffff"/>
    <polygon points="381,0 673,0 673,450 545,450 381,395" fill="var(--green)"/>
  </svg>

  <h1 class="announce">
    <span class="light">THE FOOD ACT</span><br>
    <span class="dark">2014 COMES</span><br>
    <span class="light">INTO FORCE ON</span><br>
    <span class="dark">1 MARCH 2016</span>
  </h1>
  <p class="announce-note">Food service and food retailers will be on Food Control Plans – documentation of processes and risk management to produce safe and suitable food.</p>

  <h2 class="tagline">TUNDO TRAINING – YOUR REPUTATION<span class="tagline-strong">IS OUR BUSINESS</span></h2>

  <div class="brand"><span class="brand-dot"></span><span class="brand-name">Tundo Training</span></div>

  <section class="packages">
    <div class="package package--videos">
      <h3 class="package-title"><span>VIDEOS</span></h3>
      <p class="package-text">Animated training videos of the FCP 6 month subscription Translated into Mandarin, Japanese, Korean and Hindi</p>
    </div>
    <div class="package package--webinars">
      <h3 class="package-title"><span>WEBINARS/WORKSHOPS</span></h3>
      <p class="package-text">A range of webinars at times to suit the hospitality industry AND half day training workshops. 6 month subscription to the video library is included</p>
    </div>
    <div class="package package--mentoring">
      <h3 class="package-title"><span>1-TO-1 MENTORING</span></h3>
      <p class="package-text">We come to you and go through the FCP page by page</p>
    </div>
  </section>

  <h3 class="knowledge-title">WITH UP-TO-DATE KNOWLEDGE ON:</h3>
  <div class="knowledge">
    <ul class="knowledge-list knowledge-list--first">
      <li>The Food Act 2014</li>
      <li>Food Control Plan requirements</li>
    </ul>
    <ul class="knowledge-list knowledge-list--second">
      <li>Verification expectations</li>
      <li>New Food Grading&nbsp; system</li>
      <li>New Fees</li>
    </ul>
  </div>

  <div class="call">
    <svg class="call-tab" viewBox="0 0 40 20" aria-hidden="true"><polygon points="0,20 40,0 40,20" fill="var(--orange)"/></svg>
    <p class="call-label">CALL US</p>
    <p class="call-number">987.654.32</p>
  </div>

  <div class="footer-rule"></div>
  <footer class="footer">www.tundotraining.co.nz&nbsp; | Mail - info@tundotraining.co.nz</footer>
</main>
</body>
</html>
```